KV Holding ltd*

I need a full website designed for for a 10,000m2 strorage facity which specialize in heavy commercial storage

it needs to be in english please

Target Market(s)

Comercial sector

Industry/Entity Type

Construction Company

Logo Text

KV

Coding

Coded - Design and coding required

Number of Pages Required

1 page

Font styles to use
Sans Serif

Colors
ec1f27
ffffff

Requirements
Must have
• Tel 0064 218846097
• email- lewis@kvholding.co.nz
Nice to have
• We specilize in large items with the facilty have 3 15tonne Gantry cranes and heavy mobile lifting equipment we can store items up to 20 tonne and we are fully covered and secure.
• square meter rates from 20m2 to 10,000 m2

```html
<!DOCTYPE html>
<html lang="en">
<head>
<meta charset="utf-8">
<title>KV Storage – Heavy Commercial Storage</title>
<link rel="stylesheet" href="https://fonts.googleapis.com/css2?family=Open+Sans:wght@300;400;600;700&display=swap">
<style>
:root{
  --red:#ec1f27;
  --red-light:#ef3340;
  --red-dark:#e21a22;
  --black:#000000;
  --white:#ffffff;
  --ink:#1a1a1a;
}
*{margin:0;padding:0;box-sizing:border-box}
html,body{width:864px;height:1200px;overflow:hidden;background:var(--white)}
body{font-family:"Open Sans",Arial,sans-serif;color:var(--ink);position:relative}
.abs{position:absolute;line-height:1;white-space:nowrap}

/* header */
.site-header{position:absolute;left:0;top:0;width:864px;height:34px;background:var(--black)}
.nav-link{position:absolute;top:13px;font-size:6.5px;color:var(--white);line-height:1}
.social{position:absolute;top:13px;width:10px;height:10px;border-radius:50%;background:var(--white)}
.logo-tab{position:absolute;left:370px;top:0;width:125px;height:63px;background:var(--black);border-radius:0 0 34px 34px}
.logo-name{position:absolute;left:0;top:26px;width:125px;text-align:center;font-size:13px;font-weight:600;color:var(--white);line-height:1;white-space:nowrap}

/* hero */
.hero{position:absolute;left:0;top:34px;width:864px;height:178px;
  background:linear-gradient(120deg,#c8404a 0%,#3f5a9a 30%,#d9415a 55%,#2f4f9a 75%,#e04868 100%)}
.hero-caption{position:absolute;left:186px;top:109px;width:272px;height:56px;background:rgba(40,40,40,.55)}
.hero-title{position:absolute;right:11px;top:9px;font-size:22px;color:var(--white);line-height:1}
.hero-sub{position:absolute;right:12px;top:34px;font-size:11px;color:var(--white);line-height:1}

/* section headings */
.heading{position:absolute;font-size:16px;font-weight:300;line-height:1;color:var(--ink)}
.rule{position:absolute;height:1px;background:var(--red)}

/* about */
.about-text{position:absolute;left:193px;top:297px;width:215px;font-size:7px;line-height:9.5px;color:var(--ink)}
.about-text p+p{margin-top:9px}
.about-photo{position:absolute;left:425px;top:247px;width:238px;height:117px;background:linear-gradient(90deg,#e4760a,#f59a14 45%,#c35a06)}

/* stats */
.stats{position:absolute;left:0;top:393px;width:864px;height:62px;background:var(--red)}
.stat{position:absolute;top:0;height:62px;text-align:center;color:var(--white)}
.stat-label{position:absolute;left:0;width:100%;top:10px;font-size:8px;line-height:1}
.stat-value{position:absolute;left:0;width:100%;top:17px;font-size:27px;line-height:1}
.stat-unit{position:absolute;left:0;width:100%;top:47px;font-size:7px;font-weight:700;line-height:1}

/* services */
.service-photo{position:absolute;top:539px;width:173px;height:86px}
.service-label{position:absolute;top:631px;width:173px;text-align:center;font-size:7.5px;line-height:1}

/* testimonials */
.testimonials{position:absolute;left:0;top:680px;width:864px;height:188px;background:var(--red)}
.avatar{position:absolute;width:73px;height:73px;border-radius:50%}
.client-name{position:absolute;font-size:7.5px;color:var(--white);line-height:1}
.client-role{position:absolute;font-size:6px;color:var(--white);line-height:1}
.client-quote{position:absolute;font-size:7px;line-height:12px;color:var(--white);width:160px;white-space:normal}

/* blog */
.blog-card{position:absolute;top:955px;width:169px;height:146px;background:var(--black)}
.blog-photo{position:absolute;left:0;top:0;width:169px;height:86px}
.blog-title{position:absolute;left:10px;top:95px;font-size:7.5px;font-weight:400;color:var(--red);line-height:1}
.blog-date{position:absolute;left:10px;top:106px;font-size:5.5px;color:var(--white);line-height:1}
.blog-text{position:absolute;left:10px;top:116px;width:152px;font-size:6.5px;line-height:9.5px;color:var(--white)}

/* footer */
.site-footer{position:absolute;left:0;top:1138px;width:864px;height:62px;background:var(--black)}
.footer-contact{position:absolute;left:518px;top:0;width:173px;height:62px;background:var(--red)}
.footer-link{position:absolute;left:191px;font-size:5.5px;color:var(--white);line-height:1}
.footer-right{position:absolute;right:9px;text-align:right;color:var(--white);line-height:1}
</style>
</head>
<body>

<header class="site-header">
  <span class="nav-link" style="left:216px">home</span>
  <span class="nav-link" style="left:250px">about us</span>
  <span class="nav-link" style="left:294px">contact us</span>
  <span class="nav-link" style="left:533px;top:15px">services</span>
  <span class="nav-link" style="left:573px;top:15px">facilty</span>
  <span class="social" style="left:630px" aria-label="Social link"></span>
  <span class="social" style="left:644px" aria-label="Social link"></span>
  <span class="social" style="left:658px" aria-label="Social link"></span>
  <span class="social" style="left:672px" aria-label="Social link"></span>
</header>

<section class="hero" role="img" aria-label="Aerial view of a container port with rows of colourful shipping containers">
  <div class="hero-caption">
    <span class="hero-title abs">10,000 m² strorage facity</span>
    <span class="hero-sub abs">specialize in heavy commercial storage</span>
  </div>
</section>

<div class="logo-tab">
  <span class="logo-name">KV Storage</span>
</div>

<section class="about">
  <h1 class="heading" style="left:193px;top:256px">KV STORAGE</h1>
  <div class="rule" style="left:193px;top:280px;width:42px"></div>
  <div class="about-text">
    <p>We provide 10,000m2 strorage facity which specialize in heavy commercial storage.</p>
    <p>We specilize in large items with the facilty have 3 15tonne Gantry cranes and heavy mobile lifting equipment we can store items up to 20 tonne and we are fully covered and secure.</p>
  </div>
  <div class="about-photo" role="img" aria-label="Gantry crane silhouetted against an orange sunset"></div>
</section>

<section class="stats">
  <div class="stat" style="left:172px;width:172px;background:var(--red-light)">
    <span class="stat-label">with</span>
    <span class="stat-value">3</span>
    <span class="stat-unit">15 TONNE GANTRY CRANES</span>
  </div>
  <div class="stat" style="left:344px;width:173px">
    <span class="stat-label" style="top:9px">store items up to</span>
    <span class="stat-value" style="top:16px">20</span>
    <span class="stat-unit" style="top:46px">TONNE</span>
  </div>
  <div class="stat" style="left:517px;width:174px;background:var(--red-dark)">
    <span class="stat-label">square meter rates from</span>
    <span class="stat-value">20 - 10,000</span>
    <span class="stat-unit">M²</span>
  </div>
</section>

<section class="services">
  <h2 class="heading" style="left:0;width:866px;text-align:center;top:487px">SERVICE</h2>
  <div class="rule" style="left:415px;top:513px;width:39px"></div>
  <div class="service-photo" style="left:172px;background:linear-gradient(135deg,#d9683a,#c55a30 50%,#3d4f7a)" role="img" aria-label="Stacked shipping containers"></div>
  <div class="service-photo" style="left:345px;background:linear-gradient(180deg,#4f8a4a,#5a7aa0 35%,#8a8a86)" role="img" aria-label="Aerial view of a container yard with a straddle carrier"></div>
  <div class="service-photo" style="left:518px;background:linear-gradient(135deg,#2a5a9a,#3f7ac0 50%,#2e5a3a)" role="img" aria-label="Port crane lifting a container beside stacked containers"></div>
  <span class="service-label" style="left:172px">HEAVY COMMERCIAL STORAGE</span>
  <span class="service-label" style="left:345px">FULLY COVERED</span>
  <span class="service-label" style="left:518px">SECURE</span>
</section>

<section class="testimonials">
  <h2 class="heading" style="left:0;width:862px;text-align:center;top:24px;color:var(--white)">CLIENT TESTIMONIAL</h2>
  <div class="rule" style="left:412px;top:50px;width:38px;background:var(--white)"></div>

  <div class="avatar" style="left:183px;top:85px;background:linear-gradient(160deg,#4a4e58,#d8cfc4)" role="img" aria-label="Portrait of client Peter Hollis"></div>
  <span class="client-name" style="left:269px;top:96px">PETER HOLLIS</span>
  <span class="client-role" style="left:269px;top:106px">DIRECTOR</span>
  <p class="client-quote" style="left:269px;top:117px">“Great Facility and very secure, top services by KVStorage. Keep up great works”</p>

  <div class="avatar" style="left:442px;top:86px;background:linear-gradient(160deg,#9a9a98,#c9a27a)" role="img" aria-label="Portrait of client Mara Quinn"></div>
  <span class="client-name" style="left:529px;top:96px">MARA QUINN</span>
  <span class="client-role" style="left:529px;top:106px">DIRECTOR</span>
  <p class="client-quote" style="left:529px;top:117px">“Great Facility and very secure, top services by KVStorage. Keep up great works”</p>
</section>

<section class="blog">
  <h2 class="heading" style="left:185px;top:901px">LATEST BLOG</h2>
  <div class="rule" style="left:187px;top:927px;width:38px"></div>

  <article class="blog-card" style="left:172px">
    <div class="blog-photo" style="background:linear-gradient(180deg,#6a9ad0,#4a5a78 50%,#7a4a3a)" role="img" aria-label="Container stacks under a blue sky"></div>
    <h3 class="blog-title">WHAT IS A GANTRY CRANE?</h3>
    <span class="blog-date">26 FEBRUARY 2020</span>
    <p class="blog-text">A gantry crane is a type of overhead crane with a single or double girder configuration</p>
  </article>
  <article class="blog-card" style="left:348px">
    <div class="blog-photo" style="background:linear-gradient(180deg,#3a7ad0,#c0392b 55%,#2f4f9a)" role="img" aria-label="Red and blue containers with port cranes behind"></div>
    <h3 class="blog-title">WHAT IS A GANTRY CRANE?</h3>
    <span class="blog-date">26 FEBRUARY 2020</span>
    <p class="blog-text">A gantry crane is a type of overhead crane with a single or double girder configuration</p>
  </article>
  <article class="blog-card" style="left:523px">
    <div class="blog-photo" style="background:linear-gradient(180deg,#5a6470,#8a7a60 35%,#2a3450)" role="img" aria-label="Container terminal at dusk"></div>
    <h3 class="blog-title">WHAT IS A GANTRY CRANE?</h3>
    <span class="blog-date">26 FEBRUARY 2020</span>
    <p class="blog-text">A gantry crane is a type of overhead crane with a single or double girder configuration</p>
  </article>
</section>

<footer class="site-footer">
  <span class="footer-link" style="top:17px">Terms &amp; Conditions</span>
  <span class="footer-link" style="top:26px">Privacy</span>
  <span class="footer-link" style="top:35px">Feedback</span>
  <span class="footer-link" style="top:44px">Site Map</span>

  <span class="abs" style="left:299px;top:12px;font-size:7.5px;color:var(--red)">Working Hours</span>
  <span class="abs" style="left:299px;top:28px;font-size:5.5px;color:var(--white)">Everyday</span>
  <span class="abs" style="left:299px;top:37px;font-size:5.5px;color:var(--white)">07.00 A.M - 10.00 P.M</span>

  <div class="footer-contact">
    <span class="footer-right" style="top:11px;font-size:8.5px">KV Holding ltd</span>
    <span class="footer-right" style="top:23px;font-size:6px">Tel 0064 218846097</span>
    <span class="footer-right" style="top:32px;font-size:6px">email- lewis@kvholding.co.nz</span>
    <span class="footer-right" style="top:43px;font-size:5.5px">© 2020 KV Holding ltd</span>
  </div>
</footer>

</body>
</html>
```